New Toothpaste brand needs a logo & packaging design

Our company is launching a new toothpaste and is looking for a logo and packaging design. The toothpaste brand is called Orevim. The packaging should have the same design quality as the major international brands, such as Brisa, Brisa Totalcare, Dentolux, Pavona, Kiwi-dew, Mirabel, etc. The dominant colors for our brand should be hues of blue, similar to other major brands. In addition, there should be a little bit of green to represent the "Fresh Mint Blast" flavor and the "Extracts of Aloe Vera" included in the ingredients.

There are typically 3 unique sides on a toothpaste box:

The face: Repeated on ~3 sides of the 4 faces of the box
The back: The 4th box face has the instructions for use, ingredients, company information, bar code/product info, and some branding elements.
The sides: Usually consisting of just the logo, flavor etc.

Please refer to existing brands such as Brisa, Brisa Total-care, and Dentolux for an example of typical box layout and elements.

Task Details:
Package Dimensions: 180 mm x 48 mm x 28 mm, 100 ml toothpaste tube
Brand Name: Orevim
Description: Fluoride Toothpaste
Flavor: Fresh Mint Blast
5 Actions: Protects against cavities and tartar, freshens breath, whitens teeth, and maintains healthy gums. These actions can also be made into a list like Brisa Total Care or Dentolux Max care. For instance, Strong Teeth, Fresh Breath, Whitening, Healthy Gums, Cavity and Tartar Protection.
Also contains whitening micro particles and extracts of aloe vera which may be highlighted on the package

Overall, the look should be high quality and with the same look and feel as the big brands mentioned previously. We do not have an existing logo for this brand. The face of the package is the most important element as it is often repeated on several sides and on the tube itself.

Please let me know if you have any questions.

I've attached some of our favorite big brand designs below. I would say the Brisa Total Care and 9K vers
Updates

The logos I've seen so far for Orevim, have been a bit too bold. A little bold is okay, but just needs to be moderate. 

I would like the colors to be bright and appealing. I mentioned shades of blue being the major color, but green should also be highlighted as well, perhaps in a 80% blue to 20% green ratio. 

Target Market(s)

adult consumer of toothpaste, both female and male.

Industry/Entity Type

It Company

Requirements
Must have
• A logo with the brand name: Orevim
Description or sub text: Fluoride Toothpaste
Flavor: Fresh Mint Blast
A phrase or list describing the Toothpaste Actions: e.g., Protects against cavities and tartar, freshens breath, whitens teeth, and maintains healthy gums. Or as a list simialr to Brisa Total Care or Dentolux Max Care:
-Anti-cavity
-Anti-tartar
-Fresh breath
-Whitening
-Healthy Gums

Special ingredient of "whitening micro particles: and "extracts of aloe vera", which should also be highlighted.

The color should mostly be shades of blue, with only a little bit of green to accentuate the fresh mint blast flavor and aloe vera

Nice to have
• The design should really look good next to brisa total care, 9k gleam, and dentolux max care. These are our favorite designs.
Should not have
• For aloe vera, there is no need to show the plant.

The Orevim logo shouldn't be too Bold. This should be appeal to all consumers, not just men.

```html
<!DOCTYPE html>
<html lang="en">
<head>
<meta charset="utf-8">
<title>Orevim Fluoride Toothpaste – Pack Face</title>
<link rel="stylesheet" href="https://fonts.googleapis.com/css2?family=Arimo:wght@400;700&display=swap">
<style>
  :root {
    --sky-deep: #0a3fb8;
    --sky-mid: #1f7ee6;
    --sky-light: #9fe4ff;
    --glow: #eafcff;
    --claim-green: #4fe59c;
    --claim-blue: #1d5fd6;
    --claim-edge: #2b8fe0;
    --brand-blue: #2f8fdc;
    --badge-red: #f01212;
    --mint: #5cedaa;
    --mint-edge: #36c4c0;
    --flavor-ink: #1548c4;
    --white: #ffffff;
  }
  * { margin: 0; padding: 0; box-sizing: border-box; }
  html, body { width: 1200px; height: 200px; overflow: hidden; background: var(--white); }
  .pack-face {
    position: relative;
    width: 1200px;
    height: 200px;
    overflow: hidden;
    font-family: "Arimo", Arial, sans-serif;
    background:
      radial-gradient(ellipse 420px 150px at 640px 60px, var(--glow) 0%, var(--sky-light) 30%, rgba(60,160,240,0) 75%),
      linear-gradient(90deg, var(--sky-deep) 0%, var(--sky-mid) 35%, #37a8ef 60%, var(--sky-mid) 85%, var(--sky-deep) 100%);
  }

  .claims { position: absolute; left: 0; top: 23px; list-style: none; }
  .claim {
    width: 302px;
    height: 28px;
    margin-bottom: 4.6px;
    padding-left: 10px;
    line-height: 26px;
    font-size: 17px;
    font-weight: 700;
    color: var(--white);
    border: 2px solid var(--claim-edge);
    border-left: none;
    letter-spacing: 0.2px;
  }
  .claim--green { background: var(--claim-green); }
  .claim--blue { background: var(--claim-blue); }

  .new-badge {
    position: absolute;
    left: 517px; top: 0;
    width: 133px; height: 50px;
    background: var(--badge-red);
    border-radius: 0 0 4px 4px;
    color: var(--white);
    font-size: 41px;
    font-weight: 700;
    text-align: center;
    line-height: 52px;
  }

  .brand-name {
    position: absolute;
    left: 343px; top: 44px;
    width: 500px;
    text-align: center;
    font-size: 124px;
    font-weight: 700;
    line-height: 1;
    letter-spacing: -2px;
    color: var(--brand-blue);
  }

  .product-type {
    position: absolute;
    left: 416px; top: 158px;
    width: 380px;
    text-align: center;
    font-size: 30px;
    line-height: 34px;
    font-weight: 700;
    color: var(--white);
    -webkit-text-stroke: 1.5px var(--claim-blue);
    paint-order: stroke fill;
  }

  .ingredients {
    position: absolute;
    left: 862px; top: 92px;
    width: 174px;
    font-size: 10.5px;
    line-height: 12.5px;
    color: var(--white);
    text-align: center;
  }

  .flavor-panel {
    position: absolute;
    left: 1042px; top: 30px;
    width: 140px; height: 140px;
    background: var(--mint);
    border: 3px solid var(--mint-edge);
    display: flex;
    align-items: center;
    justify-content: center;
    text-align: center;
    color: var(--flavor-ink);
    font-size: 15px;
    font-weight: 700;
    line-height: 25px;
  }
</style>
</head>
<body>
  <main class="pack-face">
    <ul class="claims">
      <li class="claim claim--green">PROTECTS AGAINST CAVITIES</li>
      <li class="claim claim--blue">PROTECTS AGAINST TARTAR</li>
      <li class="claim claim--green">FRESHENS BREATH</li>
      <li class="claim claim--blue">WHITENS TEETH</li>
      <li class="claim claim--green">MAINTAINS HEALTHY GUMS</li>
    </ul>

    <div class="new-badge">NEW</div>
    <h1 class="brand-name">OREVIM</h1>
    <p class="product-type">Fluoride Toothpaste</p>

    <p class="ingredients">contains whitening micro particles<br>and extracts of aloe vera</p>

    <div class="flavor-panel">FRESH<br>MINT<br>BLAST</div>
  </main>
</body>
</html>
```